Fern Lantern Cannabis Cartridge box

Box with both inside and outside box. A disposable cannabis vape cart is the contents of the package. initial thoughts were black exterior box with color highlight. (example of 7 mint attached). There are four colors currently being used for the actual product. Black, White, Green and Blue. product will sit in retail display box. It should both "pop" and still emote quality and class.

Target Market(s)

Professional, discreet cannabis consumer. Experienced and knowledgeable

Industry/Entity Type

Cannabis

Font styles to use
Serif

Colors

Designer to choose colors to be used in the design.

Requirements
Must have
• use logo and logo colors
Nice to have
• elegant look. metalic foil printing, embossing available

```html
<!DOCTYPE html>
<html lang="en">
<head>
<meta charset="utf-8">
<title>Fern Lantern – Blue Cartridge Box Dielines</title>
<link href="https://fonts.googleapis.com/css2?family=Exo+2:wght@300;700&display=swap" rel="stylesheet">
<style>
  :root {
    --paper: #ffffff;
    --box-black: #07080c;
    --box-navy: #0a1228;
    --accent: #29a9e1;
    --swirl-deep: #1c3fb8;
    --swirl-mid: #1d6fd6;
    --swirl-light: #2aa6e6;
    --fold: rgba(255,255,255,0.06);
  }
  html, body {
    margin: 0;
    width: 1200px;
    height: 1200px;
    overflow: hidden;
    background: var(--paper);
  }
  .canvas { display: block; width: 1200px; height: 1200px; }
  .brand-word { font-family: "Exo 2", sans-serif; font-weight: 700; fill: var(--accent); }
  .variant-label { font-family: "Exo 2", sans-serif; font-weight: 300; fill: var(--accent); letter-spacing: 3px; }
  .brand-dot { fill: none; stroke: var(--accent); stroke-width: 3; }
  .fold-line { stroke: var(--fold); stroke-width: 1.5; }
</style>
</head>
<body>
<svg class="canvas" viewBox="0 0 1200 1200" xmlns="http://www.w3.org/2000/svg">
  <defs>
    <linearGradient id="box-fill" x1="0" y1="0" x2="0" y2="1">
      <stop offset="0" stop-color="var(--box-black)"/>
      <stop offset="0.55" stop-color="#0b0a12"/>
      <stop offset="1" stop-color="var(--box-navy)"/>
    </linearGradient>
    <linearGradient id="swirl-left" x1="0" y1="640" x2="0" y2="965" gradientUnits="userSpaceOnUse">
      <stop offset="0" stop-color="#10246a" stop-opacity="0"/>
      <stop offset="0.3" stop-color="var(--swirl-deep)" stop-opacity="0.75"/>
      <stop offset="0.6" stop-color="var(--swirl-light)"/>
      <stop offset="1" stop-color="var(--swirl-mid)"/>
    </linearGradient>
    <linearGradient id="swirl-right" x1="0" y1="640" x2="0" y2="907" gradientUnits="userSpaceOnUse">
      <stop offset="0" stop-color="#10246a" stop-opacity="0"/>
      <stop offset="0.35" stop-color="var(--swirl-deep)" stop-opacity="0.8"/>
      <stop offset="0.7" stop-color="var(--swirl-light)"/>
      <stop offset="1" stop-color="var(--swirl-mid)"/>
    </linearGradient>
    <clipPath id="inner-tray-shape">
      <path d="M57 363 H105 L120 315 H191 V228 H351 V315 H420 L436 363 H486 V830 H436 L420 880 H351 V965 H191 V880 H120 L105 830 H57 Z"/>
    </clipPath>
    <clipPath id="outer-sleeve-shape">
      <path d="M552 375 L605 363 V290 H775 V303 H855 V280 H1033 V303 H1115 V365 H1122 V830 H1120 V907 H600 V830 H552 Z"/>
    </clipPath>
  </defs>

  <!-- Inner tray -->
  <g class="inner-tray">
    <path d="M57 363 H105 L120 315 H191 V228 H351 V315 H420 L436 363 H486 V830 H436 L420 880 H351 V965 H191 V880 H120 L105 830 H57 Z"
          fill="url(#box-fill)" stroke="url(#box-fill)" stroke-width="8" stroke-linejoin="round"/>
    <rect x="40" y="640" width="460" height="340" fill="url(#swirl-left)" clip-path="url(#inner-tray-shape)"
          role="img" aria-label="Swirling blue fluid-art texture"/>
    <line class="fold-line" x1="191" y1="363" x2="191" y2="830"/>
    <line class="fold-line" x1="351" y1="363" x2="351" y2="830"/>

    <text class="brand-word" x="271" y="336" font-size="38" text-anchor="middle" textLength="92" lengthAdjust="spacingAndGlyphs">FERN</text>
    <text class="brand-word" x="271" y="356" font-size="16" text-anchor="middle" textLength="84" lengthAdjust="spacing">LANTERN</text>

    <text class="brand-word" x="271" y="466" font-size="46" text-anchor="middle" textLength="110" lengthAdjust="spacingAndGlyphs">FERN</text>
    <text class="brand-word" x="271" y="490" font-size="20" text-anchor="middle" textLength="100" lengthAdjust="spacing">LANTERN</text>

    <circle class="brand-dot" cx="158" cy="452" r="20"/>
    <circle class="brand-dot" cx="382" cy="640" r="20"/>

    <text class="brand-word" font-size="30" transform="translate(152 515) rotate(90)" textLength="72" lengthAdjust="spacingAndGlyphs">FERN</text>
    <text class="brand-word" font-size="13" transform="translate(136 515) rotate(90)" textLength="72" lengthAdjust="spacing">LANTERN</text>
    <text class="variant-label" font-size="16" transform="translate(152 616) rotate(90)">BLUE</text>

    <text class="brand-word" font-size="30" transform="translate(390 588) rotate(-90)" textLength="72" lengthAdjust="spacingAndGlyphs">FERN</text>
    <text class="brand-word" font-size="13" transform="translate(406 588) rotate(-90)" textLength="72" lengthAdjust="spacing">LANTERN</text>
    <text class="variant-label" font-size="16" transform="translate(390 490) rotate(-90)">BLUE</text>

    <text class="brand-word" x="272" y="630" font-size="40" text-anchor="middle">FERN</text>
    <text class="brand-word" x="272" y="668" font-size="22" text-anchor="middle" textLength="120" lengthAdjust="spacing">LANTERN</text>
  </g>

  <!-- Outer sleeve -->
  <g class="outer-sleeve">
    <path d="M552 375 L605 363 V290 H775 V303 H855 V280 H1033 V303 H1115 V365 H1122 V830 H1120 V907 H600 V830 H552 Z"
          fill="url(#box-fill)" stroke="url(#box-fill)" stroke-width="8" stroke-linejoin="round"/>
    <rect x="545" y="640" width="585" height="280" fill="url(#swirl-right)" clip-path="url(#outer-sleeve-shape)"
          role="img" aria-label="Swirling blue fluid-art texture"/>
    <line class="fold-line" x1="605" y1="363" x2="605" y2="830"/>
    <line class="fold-line" x1="790" y1="363" x2="790" y2="907"/>
    <line class="fold-line" x1="860" y1="363" x2="860" y2="907"/>
    <line class="fold-line" x1="1030" y1="363" x2="1030" y2="907"/>

    <text class="brand-word" x="696" y="345" font-size="38" text-anchor="middle" textLength="92" lengthAdjust="spacingAndGlyphs">FERN</text>
    <text class="brand-word" x="696" y="365" font-size="16" text-anchor="middle" textLength="84" lengthAdjust="spacing">LANTERN</text>
    <text class="brand-word" x="945" y="345" font-size="38" text-anchor="middle" textLength="92" lengthAdjust="spacingAndGlyphs">FERN</text>
    <text class="brand-word" x="945" y="365" font-size="16" text-anchor="middle" textLength="84" lengthAdjust="spacing">LANTERN</text>

    <text class="brand-word" x="697" y="466" font-size="46" text-anchor="middle" textLength="110" lengthAdjust="spacingAndGlyphs">FERN</text>
    <text class="brand-word" x="697" y="490" font-size="20" text-anchor="middle" textLength="100" lengthAdjust="spacing">LANTERN</text>
    <text class="brand-word" x="945" y="466" font-size="46" text-anchor="middle" textLength="110" lengthAdjust="spacingAndGlyphs">FERN</text>
    <text class="brand-word" x="945" y="490" font-size="20" text-anchor="middle" textLength="100" lengthAdjust="spacing">LANTERN</text>

    <circle class="brand-dot" cx="832" cy="455" r="20"/>
    <circle class="brand-dot" cx="1057" cy="640" r="20"/>

    <text class="brand-word" font-size="30" transform="translate(826 515) rotate(90)" textLength="72" lengthAdjust="spacingAndGlyphs">FERN</text>
    <text class="brand-word" font-size="13" transform="translate(810 515) rotate(90)" textLength="72" lengthAdjust="spacing">LANTERN</text>
    <text class="variant-label" font-size="16" transform="translate(826 616) rotate(90)">BLUE</text>

    <text class="brand-word" font-size="30" transform="translate(1064 588) rotate(-90)" textLength="72" lengthAdjust="spacingAndGlyphs">FERN</text>
    <text class="brand-word" font-size="13" transform="translate(1080 588) rotate(-90)" textLength="72" lengthAdjust="spacing">LANTERN</text>
    <text class="variant-label" font-size="16" transform="translate(1064 490) rotate(-90)">BLUE</text>

    <text class="brand-word" x="698" y="630" font-size="40" text-anchor="middle">FERN</text>
    <text class="brand-word" x="698" y="668" font-size="22" text-anchor="middle" textLength="120" lengthAdjust="spacing">LANTERN</text>
    <text class="brand-word" x="946" y="630" font-size="40" text-anchor="middle">FERN</text>
    <text class="brand-word" x="946" y="668" font-size="22" text-anchor="middle" textLength="120" lengthAdjust="spacing">LANTERN</text>
  </g>
</svg>
</body>
</html>
```